Business card design needed

Bravoline First Aid Training is a training provider in the Canberra region. We provide both public and private course bookings.

I want my business card to be fun/interesting. I have attached my own logo, however whatever you think works best will work for me.

Please see my website for more inspiration at www.bravoline.com.au

I would like a double sided design, and round corners please.

Some really good designs so far, just not quite the right one yet. 
Please look at my website for inspiration. 
Www.bravoline.com.au

Industry/Entity Type

Training

Contact Information for Business Card

Bravoline First Aid Training, Tobin Carrow, 0498365027, tobincarrow4@mailbox-example.com.au, www.bravoline.com.au

```html
<!DOCTYPE html>
<html lang="en">
<head>
<meta charset="utf-8">
<title>Bravoline First Aid Training – Business Card</title>
<link href="https://fonts.googleapis.com/css2?family=Open+Sans:wght@400;600;700&display=swap" rel="stylesheet">
<style>
  :root {
    --page: #f1f1f1;
    --slate-top: #4f535f;
    --slate-mid: #5a5868;
    --slate-deep: #1e2026;
    --charcoal-warm: #4f4747;
    --charcoal: #373737;
    --blue-top: #3a6ca2;
    --blue-mid: #2c4a8a;
    --blue-deep: #12275a;
    --brand-red: #d6202a;
    --white: #ffffff;
    --card-w: 600px;
    --card-h: 343px;
    --radius: 14px;
  }
  * { box-sizing: border-box; margin: 0; padding: 0; }
  html, body { width: 1200px; height: 900px; overflow: hidden; }
  body {
    background: var(--page);
    font-family: "Open Sans", Arial, sans-serif;
    display: flex;
    flex-direction: column;
    align-items: center;
    justify-content: center;
    gap: 44px;
  }
  .card {
    position: relative;
    width: var(--card-w);
    height: var(--card-h);
    border-radius: var(--radius);
    overflow: hidden;
    box-shadow: 0 4px 14px rgba(0,0,0,0.18);
  }

  /* Back side */
  .back-pattern {
    position: absolute; inset: 0;
    background: linear-gradient(180deg, var(--slate-top) 0%, var(--slate-mid) 45%, var(--slate-deep) 100%);
  }
  .brand {
    position: absolute;
    display: flex; align-items: center;
    color: var(--white); font-weight: 700; line-height: 1;
  }
  .brand-dot { flex: none; border-radius: 50%; background: var(--brand-red); }
  .card-back .brand {
    left: 50%; top: 50%; transform: translate(-50%, -50%);
    font-size: 46px; gap: 12px;
  }
  .card-back .brand-dot { width: 44px; height: 44px; }

  /* Front side */
  .card-front {
    background: linear-gradient(180deg, var(--charcoal-warm) 0%, var(--charcoal) 100%);
  }
  .side-pattern {
    position: absolute; top: 0; bottom: 0; left: 77%; right: 0;
    background: linear-gradient(180deg, var(--blue-top) 0%, var(--blue-mid) 55%, var(--blue-deep) 100%);
  }
  .card-front .brand {
    left: 88.5%; top: 78%; transform: translate(-50%, -50%);
    font-size: 17px; gap: 6px;
  }
  .card-front .brand-dot { width: 14px; height: 14px; }

  .company {
    position: absolute; left: 78px; top: 70px;
    color: var(--white); font-size: 23px; font-weight: 700; letter-spacing: 0.2px;
  }
  .website {
    position: absolute; left: 112px; top: 104px;
    color: var(--white); font-size: 15px; font-weight: 400;
  }
  .contact {
    position: absolute; right: 152px; top: 208px; text-align: right;
    color: var(--white); font-size: 13px; line-height: 1.55;
  }
  .holder {
    position: absolute; right: 138px; top: 262px;
    padding: 6px 14px 6px 90px;
    background: linear-gradient(90deg, rgba(80,80,110,0) 0%, rgba(90,88,130,0.75) 100%);
    color: var(--white); font-size: 16px; font-weight: 700; letter-spacing: 0.6px;
    text-transform: uppercase;
  }
</style>
</head>
<body>
  <section class="card card-back" aria-label="Card back">
    <div class="back-pattern" role="img" aria-label="Slate grey plaid pattern background"></div>
    <div class="brand"><span class="brand-dot"></span><span>Bravoline</span></div>
  </section>

  <section class="card card-front" aria-label="Card front">
    <h1 class="company">Bravoline First Aid Training</h1>
    <p class="website">www.bravoline.com.au</p>
    <p class="contact">0498365027<br>tobincarrow4@mailbox-example.com.au</p>
    <p class="holder">Tobin Carrow</p>
    <div class="side-pattern" role="img" aria-label="Blue plaid pattern panel"></div>
    <div class="brand"><span class="brand-dot"></span><span>Bravoline</span></div>
  </section>
</body>
</html>
```